Pura Senda Trek Holidays Rack Card

We need a double sided rack card design. One side should be promoting our "Seven Trail Days" tour with the flip side promoting our "Honeymoon" and "Custom & Family Tours". Colours should be in line with our website www.PuraSendaTrek.example. Text and photos attached (feel free to use as necessary). We are looking for a fun rack card that will catch clients eyes and hopefully promote Costa Rica as a fun and exciting vacation.

Target Market(s)

Tourism - USA and Canada

Industry/Entity Type

Tourism

Font styles to use
Sans Serif

Colors
0455a3
33a6d7
f37122

Requirements
Must have
• Our logo on both sides of the rack card. Must be bright and fun looking. Costa Rica is an outdoor destination with tons of fun activities to do, we want to try and get that feeling across on the card.
Nice to have
• I have added a price sticker to the attachments on this project. Is it possible to have something similar on the Seven Trail Days side? The price would be $1999 scored out with the new price being $1649.

```html
<!DOCTYPE html>
<html lang="en">
<head>
<meta charset="utf-8">
<title>Pura Senda Trek Holidays – Rack Card</title>
<link rel="stylesheet" href="https://fonts.googleapis.com/css2?family=Lato:wght@400;700;900&family=Great+Vibes&family=Roboto+Slab:wght@700&display=swap">
<style>
  :root {
    --brand-navy: #0455a3;
    --brand-sky: #33a6d7;
    --brand-orange: #f37122;
    --ink: #2b2b2b;
    --paper: #ffffff;
    --stage: #3b3b3b;
  }
  * { box-sizing: border-box; margin: 0; padding: 0; }
  html, body { width: 1200px; height: 907px; overflow: hidden; }
  body {
    background: var(--stage);
    font-family: "Lato", Arial, sans-serif;
    color: var(--ink);
    position: relative;
  }
  .rack-card {
    position: absolute;
    top: 62px;
    width: 363px;
    height: 788px;
    overflow: hidden;
    background: var(--paper);
  }
  .rack-card--tour { left: 183px; }
  .rack-card--about { left: 652px; }
  .card-art { position: absolute; inset: 0; width: 363px; height: 788px; }

  .brand-mark {
    position: absolute;
    left: 58px;
    top: 244px;
    display: flex;
    align-items: center;
    gap: 7px;
    font-weight: 700;
    font-size: 19px;
    letter-spacing: 2px;
    color: var(--brand-orange);
    text-transform: uppercase;
  }
  .brand-mark__dot {
    width: 14px; height: 14px; border-radius: 50%;
    background: var(--brand-sky);
  }

  /* Tour side */
  .tour-title {
    position: absolute; left: 0; right: 0; top: 308px;
    text-align: center;
    font-weight: 700; font-size: 28px; letter-spacing: .5px;
    color: var(--brand-navy);
  }
  .tour-title span { color: var(--ink); }
  .tour-band {
    position: absolute; left: 0; right: 0; top: 358px; height: 31px;
    background: var(--brand-navy);
    color: var(--brand-orange);
    text-align: center;
    font-weight: 900; font-size: 19px; line-height: 31px; letter-spacing: .3px;
  }
  .tour-intro {
    position: absolute; left: 20px; right: 20px; top: 401px;
    text-align: center; font-weight: 700; font-size: 12.5px; line-height: 15px;
  }
  .section-pill {
    position: absolute; height: 24px;
    background: var(--brand-orange);
    border-radius: 12px;
    color: var(--paper);
    font-family: "Roboto Slab", Georgia, serif;
    font-weight: 700; font-size: 15px; letter-spacing: 1.5px;
    text-align: center; line-height: 24px;
    box-shadow: 0 2px 0 rgba(0,0,0,.12);
  }
  .rack-card--tour .section-pill { left: 107px; width: 150px; top: 441px; }
  .rack-card--about .section-pill { left: 103px; width: 147px; top: 398px; }
  .itinerary {
    position: absolute; left: 24px; right: 16px; top: 473px;
    list-style: none; font-size: 13px; line-height: 16px;
  }
  .itinerary li { margin-bottom: 5px; }
  .itinerary .day { color: var(--brand-navy); }

  .photo-circle {
    position: absolute; border-radius: 50%;
    border: 4px solid var(--brand-orange);
  }

  .contact {
    position: absolute; right: 14px;
    list-style: none; text-align: right;
    color: var(--paper); font-size: 11px; line-height: 15.5px;
  }
  .contact li { display: flex; justify-content: flex-end; align-items: center; gap: 6px; }
  .contact svg { width: 9px; height: 9px; }

  /* About side */
  .about-script {
    position: absolute; left: 0; right: 0; top: 306px;
    text-align: center;
    font-family: "Great Vibes", cursive;
    font-weight: 400;
    font-size: 32px; color: var(--ink);
  }
  .about-title {
    position: absolute; left: 0; right: 0; top: 350px;
    text-align: center; font-size: 27px; font-weight: 400; letter-spacing: .5px;
    color: var(--brand-navy);
  }
  .about-copy {
    position: absolute; left: 26px; right: 25px; top: 433px;
    font-size: 12.6px; line-height: 16px; text-align: justify;
  }
  .follow {
    position: absolute; left: 26px; top: 753px;
    display: flex; align-items: center; gap: 4px;
    color: var(--paper); font-size: 10.5px;
  }
  .follow .social { width: 9px; height: 9px; border-radius: 50%; background: var(--brand-orange); }
  .follow .label { margin-right: 6px; }
</style>
</head>
<body>

<section class="rack-card rack-card--tour">
  <svg class="card-art" viewBox="0 0 363 788">
    <defs>
      <linearGradient id="raftPhoto" x1="0" y1="0" x2="1" y2="1">
        <stop offset="0" stop-color="#2f5a2a"/>
        <stop offset=".45" stop-color="#6f8a6a"/>
        <stop offset=".75" stop-color="#3b8fd0"/>
        <stop offset="1" stop-color="#cfe4f2"/>
      </linearGradient>
      <linearGradient id="bodyTintA" x1="0" y1="0" x2="0" y2="1">
        <stop offset="0" stop-color="#ffffff"/>
        <stop offset=".5" stop-color="#f1f7fc"/>
        <stop offset="1" stop-color="#dceaf6"/>
      </linearGradient>
      <linearGradient id="footBlueA" x1="0" y1="0" x2="1" y2="1">
        <stop offset="0" stop-color="#1f6fc0"/>
        <stop offset="1" stop-color="#0455a3"/>
      </linearGradient>
      <radialGradient id="waveArtA" cx=".5" cy=".5" r=".5">
        <stop offset="0" stop-color="#ffffff"/>
        <stop offset=".6" stop-color="#7fc8ea"/>
        <stop offset="1" stop-color="#33a6d7"/>
      </radialGradient>
    </defs>
    <rect x="0" y="0" width="363" height="268" fill="url(#raftPhoto)" role="img" aria-label="Photo: rafters paddling a blue raft through whitewater beside a large boulder in the jungle"/>
    <path d="M0 252 C50 226 130 222 200 238 C260 252 320 250 363 226 L363 788 L0 788 Z" fill="url(#bodyTintA)"/>
    <path d="M0 276 C40 292 120 298 200 286 C280 274 330 246 363 226" fill="none" stroke="#f37122" stroke-width="5"/>
    <path d="M0 285 C60 300 140 302 210 292" fill="none" stroke="#33a6d7" stroke-width="2"/>
    <circle cx="330" cy="218" r="32" fill="url(#waveArtA)" role="img" aria-label="Illustration: curling blue ocean wave"/>
    <path d="M0 736 C200 734 310 720 363 632 L363 788 L0 788 Z" fill="url(#footBlueA)"/>
    <path d="M0 728 C200 726 310 712 363 624" fill="none" stroke="#f37122" stroke-width="5"/>
  </svg>

  <div class="brand-mark"><span class="brand-mark__dot"></span>Pura Senda</div>

  <h1 class="tour-title">SEVEN <span>TRAIL DAYS</span></h1>
  <div class="tour-band">8 DAYS, 8 ADVENTURES, 1 LIFE</div>
  <p class="tour-intro">Come join us in the tropics on one of our all inclusive<br>8 day Seven Trail Days tours</p>
  <div class="section-pill">ITINERARY</div>
  <ul class="itinerary">
    <li><span class="day">Day 1</span> – Pick Up San Jose International Airport</li>
    <li><span class="day">Day 2</span> – Beginner Kayaking</li>
    <li><span class="day">Day 3</span> – Whitewater Rafting. Overnight Jungle Lodge</li>
    <li><span class="day">Day 4</span> – Canopy/Zipline Tour &amp; Jungle Hikes. Overnight Jungle Lodge</li>
    <li><span class="day">Day 5</span> – Whitewater Rafting &amp; Beach</li>
    <li><span class="day">Day 6</span> – Surfing &amp; Snorkeling</li>
    <li><span class="day">Day 7</span> – Canyoning (Rappelling Waterfalls) or Mountain Biking. Your choice!</li>
    <li><span class="day">Day 8</span> – Drop Off San Jose International Airport</li>
  </ul>

  <div class="photo-circle" role="img" aria-label="Photo: traveller on a jungle zipline" style="left:10px;top:696px;width:84px;height:84px;background:radial-gradient(circle at 50% 45%,#7fae4a,#2f5d22);"></div>
  <div class="photo-circle" role="img" aria-label="Photo: canyoner rappelling down a waterfall" style="left:102px;top:690px;width:78px;height:78px;background:radial-gradient(circle at 50% 45%,#8a8a62,#3a4a2c);"></div>

  <ul class="contact" style="top:726px;">
    <li>info@PuraSendaTrek.example
      <svg viewBox="0 0 10 10"><rect x="0.5" y="1.5" width="9" height="7" fill="#f37122"/><path d="M0.5 1.5 L5 5.5 L9.5 1.5" fill="none" stroke="#fff" stroke-width="1"/></svg></li>
    <li>1-888-555-0142
      <svg viewBox="0 0 10 10"><path d="M2 0.5 L4 0.5 L4.5 3 L3.2 4 C3.8 5.5 4.6 6.3 6 6.8 L7 5.5 L9.5 6 L9.5 8 C9.5 9 8.5 9.5 7.5 9.5 C4 9 1 6 0.5 2.5 C0.5 1.5 1 0.5 2 0.5 Z" fill="#f37122"/></svg></li>
    <li>www.PuraSendaTrek.example
      <svg viewBox="0 0 10 10"><circle cx="5" cy="5" r="4.5" fill="#f37122"/></svg></li>
  </ul>
</section>

<section class="rack-card rack-card--about">
  <svg class="card-art" viewBox="0 0 363 788">
    <defs>
      <linearGradient id="sunsetPhoto" x1="0" y1="0" x2="0" y2="1">
        <stop offset="0" stop-color="#3c5a8a"/>
        <stop offset=".35" stop-color="#c87a6a"/>
        <stop offset=".6" stop-color="#f2a04a"/>
        <stop offset="1" stop-color="#8a5a3a"/>
      </linearGradient>
      <linearGradient id="bodyTintB" x1="0" y1="0" x2="0" y2="1">
        <stop offset="0" stop-color="#ffffff"/>
        <stop offset=".7" stop-color="#f6fafd"/>
        <stop offset="1" stop-color="#dceaf6"/>
      </linearGradient>
      <linearGradient id="footBlueB" x1="0" y1="0" x2="1" y2="1">
        <stop offset="0" stop-color="#1f6fc0"/>
        <stop offset="1" stop-color="#0455a3"/>
      </linearGradient>
      <radialGradient id="waveArtB" cx=".5" cy=".5" r=".5">
        <stop offset="0" stop-color="#ffffff"/>
        <stop offset=".6" stop-color="#7fc8ea"/>
        <stop offset="1" stop-color="#33a6d7"/>
      </radialGradient>
    </defs>
    <rect x="0" y="0" width="363" height="268" fill="url(#sunsetPhoto)" role="img" aria-label="Photo: couple holding hands walking into the sea at sunset"/>
    <path d="M0 252 C50 226 130 222 200 238 C260 252 320 250 363 226 L363 788 L0 788 Z" fill="url(#bodyTintB)"/>
    <path d="M0 276 C40 292 120 298 200 286 C280 274 330 246 363 226" fill="none" stroke="#f37122" stroke-width="5"/>
    <path d="M0 285 C60 300 140 302 210 292" fill="none" stroke="#33a6d7" stroke-width="2"/>
    <circle cx="330" cy="218" r="32" fill="url(#waveArtB)" role="img" aria-label="Illustration: curling blue ocean wave"/>
    <path d="M0 698 C150 692 290 668 363 608 L363 788 L0 788 Z" fill="url(#footBlueB)"/>
    <path d="M0 690 C150 684 290 660 363 600" fill="none" stroke="#f37122" stroke-width="5"/>
  </svg>

  <div class="brand-mark"><span class="brand-mark__dot"></span>Pura Senda</div>

  <h2 class="about-script">Honeymoons &amp; Custom and</h2>
  <h2 class="about-title">FAMILY TOURS</h2>
  <div class="section-pill">ABOUT US</div>
  <p class="about-copy">Pura Senda has been specializing in helping plan unique tropical getaways since 1995. Based in Costa Rica 365 days a year, we are able to recommend the best activities, hotels and destinations to suit your vacation/honeymoon desires. We have personally explored and enjoyed many of the region’s attractions and know which ones will give you the best experience while you are here. Let us know what you are looking for and we’ll come up with an incredible itinerary, just for you!</p>

  <div class="photo-circle" role="img" aria-label="Photo: children in snorkel masks on the beach" style="left:6px;top:612px;width:110px;height:110px;background:radial-gradient(circle at 50% 45%,#f0b07a,#3a9ad0);"></div>
  <div class="photo-circle" role="img" aria-label="Photo: friends jumping on the beach at sunset" style="left:139px;top:618px;width:88px;height:88px;background:radial-gradient(circle at 50% 45%,#f2b060,#6a3a2a);"></div>
  <div class="photo-circle" role="img" aria-label="Photo: sloth hanging in a tree" style="left:238px;top:592px;width:82px;height:82px;background:radial-gradient(circle at 50% 45%,#b9a27a,#4f7a3a);"></div>

  <div class="follow"><span class="label">Follow us on</span><span class="social"></span><span class="social"></span><span class="social"></span><span class="social"></span></div>

  <ul class="contact" style="top:715px;">
    <li>info@PuraSendaTrek.example
      <svg viewBox="0 0 10 10"><rect x="0.5" y="1.5" width="9" height="7" fill="#f37122"/><path d="M0.5 1.5 L5 5.5 L9.5 1.5" fill="none" stroke="#fff" stroke-width="1"/></svg></li>
    <li>1-888-555-0142
      <svg viewBox="0 0 10 10"><path d="M2 0.5 L4 0.5 L4.5 3 L3.2 4 C3.8 5.5 4.6 6.3 6 6.8 L7 5.5 L9.5 6 L9.5 8 C9.5 9 8.5 9.5 7.5 9.5 C4 9 1 6 0.5 2.5 C0.5 1.5 1 0.5 2 0.5 Z" fill="#f37122"/></svg></li>
    <li>www.PuraSendaTrek.example
      <svg viewBox="0 0 10 10"><circle cx="5" cy="5" r="4.5" fill="#f37122"/></svg></li>
  </ul>
</section>

</body>
</html>
```